Direct Mail Postcard- Lighting Company

Our task is to send a postcard directly to houses surrounding where our company has done work. My goal is to position ourselves as the go to outdoor lighting partner for their neighborhood.
Trusted Lighting Design & Maintenance Your neighbor chose us to enhance and maintain their home's beauty and security. Now, we're offering our top-tier services to the entire neighborhood.
Please emphasize our:
Maintenance Excellence:
Regular system check-ups
Prompt repair and replacement
Upgrades to the latest technology
Less emphasis on:
Our Services:
High-Quality Landscape & Architectural Lighting
Reliable Permanent Lighting Solutions
Call us today and take advantage of our 25% discount (limited time offer)
For more details or to schedule a consultation, visit glowcrest-mo.com or call .
*Need to be able to tweak this for future campaigns. Quickly edit verbiage for future marketing campaigns. I.e. a file that can be edited through Canva
*Inspiration photo file (Yard Beacon Concepts)
*Would like to incorporate the before and after png
Call: (816) 555-0193
glowcrest-mo.com
Updates
I attached a new before and after photo. Please create a design implementing this
Look and feel
Each slider illustrates characteristics of the customer's brand and the style your logo design should communicate.

```html
<!DOCTYPE html>
<html lang="en">
<head>
<meta charset="UTF-8">
<title>Glowcrest Lighting – Neighborhood Postcard</title>
<link href="https://fonts.googleapis.com/css2?family=Barlow:wght@400;500;600;700&family=Jost:wght@300&display=swap" rel="stylesheet">
<style>
  :root {
    --gold: #b9a160;
    --black: #000000;
    --white: #ffffff;
    --ink: #1a1a1a;
    --backdrop: #a9a9a9;
    --fold: #2b2b2b;
  }
  * { margin: 0; padding: 0; box-sizing: border-box; }
  html, body { width: 1200px; height: 1200px; overflow: hidden; }
  body {
    background: var(--backdrop);
    font-family: "Barlow", Arial, sans-serif;
    color: var(--ink);
    position: relative;
  }
  .flyer {
    position: absolute;
    left: 235px; top: 84px;
    width: 730px; height: 1031px;
    background: var(--white);
    overflow: hidden;
  }
  .flyer-shapes { position: absolute; inset: 0; width: 730px; height: 1031px; }

  .brand {
    position: absolute; left: 400px; top: 70px; width: 310px;
    text-align: center; color: var(--gold);
    font-family: "Jost", Arial, sans-serif; font-weight: 300;
  }
  .brand-name { font-size: 50px; letter-spacing: 6px; line-height: 1; display: block; }
  .brand-sub { font-size: 34px; letter-spacing: 14px; line-height: 1; display: block; margin-top: 12px; }

  .headline { position: absolute; left: 41px; top: 508px; text-transform: uppercase; line-height: 1; }
  .headline-lead { display: block; font-size: 56px; font-weight: 400; color: var(--black); letter-spacing: 1px; }
  .headline-line { display: block; font-size: 37px; font-weight: 400; color: var(--gold); margin-top: 9px; letter-spacing: 0.5px; }
  .headline-line strong { font-weight: 700; }
  .headline-line.dark { color: var(--black); font-weight: 700; }

  .intro {
    position: absolute; left: 41px; top: 718px; width: 300px;
    font-size: 13.6px; line-height: 17.5px; color: var(--ink);
  }

  .contact { position: absolute; left: 41px; top: 893px; color: var(--white); }
  .contact-note { font-size: 13.6px; line-height: 17.5px; width: 320px; }
  .contact-list { list-style: none; margin-top: 24px; }
  .contact-list li { display: flex; align-items: center; gap: 16px; font-size: 21px; font-weight: 600; line-height: 28px; }
  .contact-list svg { width: 13px; height: 13px; flex: none; }

  .panel { position: absolute; left: 408px; width: 322px; padding-left: 20px; }
  .panel-title { font-size: 21px; font-weight: 500; line-height: 1; }
  .panel ul { list-style: none; margin-top: 10px; }
  .panel li { position: relative; padding-left: 33px; font-size: 13.4px; line-height: 16px; margin-bottom: 7px; }
  .panel li::before { content: "•"; position: absolute; left: 16px; }
  .panel-services { top: 489px; height: 149px; padding-top: 17px; color: var(--white); }
  .panel-services li { padding-left: 33px; }
  .panel-maintenance { top: 638px; height: 127px; padding-top: 18px; color: var(--white); }
  .panel-maintenance ul { margin-top: 14px; }
  .panel-maintenance li { margin-bottom: 8px; }

  .offer { position: absolute; left: 427px; top: 839px; }
  .offer-lead { font-size: 13.6px; line-height: 17.5px; width: 270px; }
  .offer-deal { display: flex; align-items: baseline; margin-top: 8px; line-height: 1; }
  .offer-percent { font-size: 74px; font-weight: 700; color: var(--gold); letter-spacing: -1px; }
  .offer-word { font-size: 29px; font-weight: 700; color: var(--black); margin-left: 14px; }
  .offer-note { font-size: 13px; line-height: 1; margin-top: -2px; }
</style>
</head>
<body>
  <main class="flyer">
    <svg class="flyer-shapes" viewBox="0 0 730 1031" aria-hidden="false">
      <defs>
        <linearGradient id="dayPhoto" x1="0" y1="0" x2="0" y2="1">
          <stop offset="0" stop-color="#3c4a2c"/>
          <stop offset="0.45" stop-color="#6b4a34"/>
          <stop offset="0.75" stop-color="#5f7f2e"/>
          <stop offset="1" stop-color="#4c6e22"/>
        </linearGradient>
        <linearGradient id="nightPhoto" x1="0" y1="0" x2="1" y2="1">
          <stop offset="0" stop-color="#14120e"/>
          <stop offset="0.45" stop-color="#8a5a26"/>
          <stop offset="0.7" stop-color="#3a2c18"/>
          <stop offset="1" stop-color="#161712"/>
        </linearGradient>
      </defs>
      <polygon role="img" aria-label="Photo of a brick home with landscape lighting along the garden and lawn at dusk" points="0,0 428,0 259,356 0,356" fill="url(#dayPhoto)"/>
      <polygon role="img" aria-label="Photo of a home at night with uplit trees and illuminated entryway" points="353,185 730,185 730,489 228,489" fill="url(#nightPhoto)"/>
      <polygon points="0,391 268,391 248,441 0,441" fill="var(--gold)"/>
      <rect x="408" y="489" width="322" height="149" fill="var(--gold)"/>
      <rect x="408" y="638" width="322" height="127" fill="var(--black)"/>
      <polygon points="388,622 408,612 408,762 388,753" fill="var(--fold)"/>
      <polygon points="408,765 715,765 408,795" fill="var(--gold)"/>
      <polygon points="0,876 218,838 218,850 0,884" fill="var(--gold)"/>
      <polygon points="0,884 372,838 372,1031 0,1031" fill="var(--black)"/>
    </svg>

    <header class="brand">
      <span class="brand-name">GLOWCREST</span>
      <span class="brand-sub">LIGHTING</span>
    </header>

    <h1 class="headline">
      <span class="headline-lead">Elevate</span>
      <span class="headline-line">Your <strong>Outdoor</strong></span>
      <span class="headline-line"><strong>Spaces</strong> With</span>
      <span class="headline-line dark">Premium Lighting</span>
    </h1>

    <p class="intro">Trusted Lighting Design &amp; Maintenance Your neighbor chose us to enhance and maintain their home's beauty and security. Now, we're offering our top-tier services to the entire neighborhood.</p>

    <section class="panel panel-services">
      <h2 class="panel-title">Our Services:</h2>
      <ul>
        <li>High-Quality Landscape &amp; Architectural Lighting</li>
        <li>Reliable Permanent Lighting Solutions</li>
      </ul>
    </section>

    <section class="panel panel-maintenance">
      <h2 class="panel-title">Maintenance Excellence:</h2>
      <ul>
        <li>Regular system check-ups</li>
        <li>Prompt repair and replacement</li>
        <li>Upgrades to the latest technology</li>
      </ul>
    </section>

    <section class="offer">
      <p class="offer-lead">Reach out today to schedule your appointment and take advantage of our</p>
      <p class="offer-deal"><span class="offer-percent">25%</span><span class="offer-word">discount</span></p>
      <p class="offer-note">(limited time offer)</p>
    </section>

    <footer class="contact">
      <p class="contact-note">For more details or to schedule a consultation, visit glowcrest-mo.com or call .</p>
      <ul class="contact-list">
        <li>
          <svg viewBox="0 0 24 24"><path fill="var(--gold)" d="M6.6 10.8a15.1 15.1 0 0 0 6.6 6.6l2.2-2.2c.3-.3.7-.4 1-.2 1.1.4 2.3.6 3.6.6.6 0 1 .4 1 1V20c0 .6-.4 1-1 1C10.6 21 3 13.4 3 4c0-.6.4-1 1-1h3.5c.6 0 1 .4 1 1 0 1.3.2 2.5.6 3.6.1.3 0 .7-.2 1z"/></svg>
          (816) 555-0193
        </li>
        <li>
          <svg viewBox="0 0 24 24"><circle cx="12" cy="12" r="10" fill="none" stroke="var(--gold)" stroke-width="2.4"/><path d="M2 12h20M12 2c3 3 3 17 0 20M12 2c-3 3-3 17 0 20" fill="none" stroke="var(--gold)" stroke-width="2"/></svg>
          glowcrest-mo.com
        </li>
      </ul>
    </footer>
  </main>
</body>
</html>
```